2 Funky Pages + EASY stock logo = Construction Website

We would like a funky new website - Just 2 pages - to promote our project management company. A logo is also needed, but we'll provide a stock image which just needs a colour change a text added.

Here are the instructions:

"Hollow Fern Builders"

#logo
The one I'd like is attached. Please change font and positioning of text though.

Tagline is "Don't be normal - Be clever"

#Colour combo
756897 Wood Veneer
D5D6D2 sand dollar
353C3F charcoal
962715 brick red

#Home - Page 1

Our cost-price home build service will save you thousands.
No, seriously - Here's how we do it (button)

- Pay what the home building companies do.
- HFB will manage the entire project.
- Use Stonequay Guaranteed builders and materials.
- Tender for the best industry rates.
- Get a full budget calculated for the build.
- Avoid inflated 'Fixed-price' builds.
See how it works (button)

Contact Us: 0800 617 280
enquire - Name, Phone, email, comment - SEND

#How it works - Page 2

Traditional fixed price contracts are popular because it means that any risk of unexpected problems is carried by the home builder, but the builder will generally load the price about 10 times above the actual risk carried.

It's like an over-priced insurance policy, on steroids.

Clever people do things differently.

Here's how a cost-price build works...

1) Tell us what you want to build. Dream home, townhouse, investment property, whatever.

2) We'll put a design together for you, or you can choose from a bunch of plans we've already got.

3) We'll give you a conservative price estimate.

4) We finish tweaking your plans, then send them out to our network of more than 200 builders, subcontractors and tradesmen.

5) We collect the quotes, pick the best prices, and finalise your budget. Now you buy us beer, cause you've finally realised how much you're saving.

6) Tell your friends how awesome we are, while we lodge your building consent application with Council.

7) We coordinate the builders and subbies (look, you're already speaking trade-talk) from start to finish. You pay the cost price on their work each month.

We're happy to talk numbers and give you an estimate.

Contact Us: 0800 617 280

Reason: I have seen some great design elements, but need them to come together in one site design. Also, there appears to be less attention paid to the second page design ('how it works') than is necessary... There is no viable contender there yet, compared with the great home page submissions. I've also added some further info to the brief, and note that many submissions have ignored the colour combo I've requested.

Industry/Entity Type

Construction

Number of Pages Required

2 page

Requirements
Must have
• Stonequayer logo (small)
• Colour combo described in brief.
Nice to have
• I've attached a stock image I like, but it's certainly not essential. I do like images with clear backgrounds though - they tend to produce a crisp looking site.
• There is a wider image similar to this, available on Vorlin Imagery, but Pitchwell Hub won't let me attach it.
Should not have
• Photos of cheesy American faces.

```html
<!DOCTYPE html>
<html lang="en">
<head>
<meta charset="utf-8">
<title>Hollow Fern Builders – How it Works</title>
<link rel="stylesheet" href="https://fonts.googleapis.com/css2?family=Montserrat:wght@300;400;500;600;700&family=Oswald:wght@300&display=swap">
<style>
:root{
  --brick:#962715;
  --brick-dark:#7a1f10;
  --veneer:#756897;
  --sand:#d5d6d2;
  --charcoal:#353c3f;
  --charcoal-deep:#2a3033;
  --text:#353c3f;
  --white:#ffffff;
}
*{box-sizing:border-box;margin:0;padding:0}
html,body{width:1200px;height:3163px;overflow:hidden;background:var(--white)}
body{position:relative;font-family:"Montserrat",Arial,sans-serif;color:var(--text)}

/* header */
.site-header{position:absolute;left:0;top:0;width:1200px;height:88px;background:var(--white)}
.brand-mark{position:absolute;left:160px;top:17px;width:58px;height:58px;background:var(--brick)}
.brand-name{position:absolute;left:253px;top:26px;font-size:23px;font-weight:600;color:var(--brick);line-height:1;white-space:nowrap}
.brand-tag{position:absolute;left:254px;top:56px;font-size:13px;font-weight:500;color:var(--charcoal);line-height:1;white-space:nowrap}
.header-phone{position:absolute;left:685px;top:42px;font-size:15px;color:var(--charcoal);display:flex;align-items:center;gap:8px;line-height:1;white-space:nowrap}
.btn-outline{position:absolute;left:867px;top:35px;width:183px;height:34px;border:2px solid var(--charcoal);font-size:11px;font-weight:700;letter-spacing:.5px;color:var(--charcoal);display:flex;align-items:center;justify-content:center;gap:10px;text-transform:uppercase;white-space:nowrap}

/* hero */
.hero{position:absolute;left:0;top:88px;width:1200px;height:275px;background:linear-gradient(180deg,#5c6467 0%,#858c8f 45%,#555d60 100%)}
.hero-title{position:absolute;left:0;width:1200px;top:104px;text-align:center;color:var(--white);font-size:33px;font-weight:700;letter-spacing:.5px;line-height:1;white-space:nowrap}
.hero-sub{position:absolute;left:0;width:1200px;top:148px;text-align:center;color:var(--white);font-size:17px;font-weight:400;line-height:1}
.hero-badge{position:absolute;left:564px;top:338px;width:72px;height:78px}

.intro{position:absolute;left:170px;top:446px;width:860px;text-align:center;font-size:18px;font-weight:300;line-height:24px;color:var(--veneer)}

.section-title{position:absolute;left:158px;top:612px;width:886px;height:20px}
.section-title::before{content:"";position:absolute;left:0;right:0;top:10px;border-top:1px solid var(--sand)}
.section-title span{position:absolute;left:50%;transform:translateX(-50%);background:var(--white);padding:0 22px;font-size:14px;font-weight:500;color:var(--charcoal);line-height:20px;white-space:nowrap}

/* steps */
.step-photo{position:absolute;width:220px;height:250px;clip-path:polygon(50% 0,100% 25%,100% 75%,50% 100%,0 75%,0 25%)}
.guides{position:absolute;width:300px;height:300px}
.step-num{position:absolute;font-family:"Oswald",Arial,sans-serif;font-weight:300;font-size:44px;color:var(--brick);line-height:1}
.step-text{position:absolute;font-size:14px;line-height:20px;color:var(--charcoal);white-space:nowrap}
.step-text.right{text-align:right;right:612px}

/* call band */
.cta-band{position:absolute;left:0;top:2463px;width:1200px;height:163px;background:var(--brick)}
.cta-title{position:absolute;left:0;width:1200px;top:40px;text-align:center;color:var(--white);font-size:25px;font-weight:600;line-height:1;white-space:nowrap}
.cta-btn{position:absolute;left:529px;top:89px;width:142px;height:34px;border:2px solid var(--sand);font-size:13px;font-weight:600;color:var(--white);display:flex;align-items:center;justify-content:center;gap:10px;text-transform:uppercase;letter-spacing:.5px}

/* footer */
.site-footer{position:absolute;left:0;top:2626px;width:1200px;height:474px;background:linear-gradient(180deg,#4a5255 0%,var(--charcoal) 55%,var(--charcoal-deep) 100%)}
.footer-heading{position:absolute;font-size:14px;font-weight:700;color:var(--white);line-height:1;white-space:nowrap}
.footer-heading::after{content:"";display:block;width:30px;height:2px;background:var(--white);margin-top:12px}
.field{position:absolute;left:156px;width:281px;height:30px;border:1px solid var(--sand);font-size:12px;color:var(--sand);padding:8px 10px;line-height:1}
.field.message{height:94px}
.send-btn{position:absolute;left:156px;top:362px;width:186px;height:30px;background:var(--brick);color:var(--white);font-size:11px;font-weight:700;text-transform:uppercase;display:flex;align-items:center;justify-content:center;gap:8px;white-space:nowrap}
.footer-divider{position:absolute;left:510px;top:20px;width:1px;height:350px;background:var(--veneer)}
.contact-row{position:absolute;left:588px;display:flex;gap:16px;color:var(--white);line-height:1;white-space:nowrap}
.contact-row .name{font-size:15px;font-weight:600}
.contact-row .addr{font-size:13px;color:var(--sand);margin-top:5px;line-height:17px}
.badge{position:absolute;left:915px;top:0;width:127px;height:221px}

.bottom-bar{position:absolute;left:0;top:3100px;width:1200px;height:63px;background:var(--white)}
.copyright{position:absolute;left:156px;top:32px;font-size:12px;color:var(--charcoal);white-space:nowrap}
.to-top{position:absolute;left:1092px;top:-19px;width:38px;height:38px;border-radius:50%;background:var(--charcoal)}
</style>
</head>
<body>

<header class="site-header">
  <div class="brand-mark"></div>
  <div class="brand-name">Hollow Fern Builders</div>
  <div class="brand-tag">Don't be normal - Be clever</div>
  <div class="header-phone">
    <svg width="16" height="18" viewBox="0 0 16 18"><rect x="3" y="1" width="10" height="16" rx="2" fill="none" stroke="#962715" stroke-width="2"/><rect x="6" y="13" width="4" height="2" fill="#962715"/></svg>
    0800 617 280
  </div>
  <div class="btn-outline">See how it works
    <svg width="12" height="12" viewBox="0 0 12 12"><circle cx="6" cy="6" r="6" fill="#353c3f"/><path d="M5 3.5 7.5 6 5 8.5" stroke="#fff" stroke-width="1.5" fill="none"/></svg>
  </div>
</header>

<section class="hero" role="img" aria-label="Architectural plans, drafting tools and a house frame under construction">
  <h1 class="hero-title">CLEVER PEOPLE DO THINGS DIFFERENTLY.</h1>
  <p class="hero-sub">Here's how a cost-price build works ...</p>
</section>
<svg class="hero-badge" viewBox="0 0 72 78"><polygon points="36,0 72,19.5 72,58.5 36,78 0,58.5 0,19.5" fill="#353c3f"/><path d="M30 36 36 42 42 36" stroke="#d5d6d2" stroke-width="2.5" fill="none"/></svg>

<p class="intro">Traditional fixed price contracts are popular because it means that any risk of<br>unexpected problems is carried by the home builder, but the builder will generally load the<br>price about 10 times above the actual risk carried. It's like an over-priced<br>insurance policy, on steroids.</p>

<div class="section-title"><span>How it Works ?</span></div>

<!-- step 1 -->
<svg class="guides" style="left:186px;top:680px" viewBox="0 0 300 300"><g stroke="#d5d6d2" stroke-width="1"><line x1="0" y1="40" x2="300" y2="40"/><line x1="0" y1="270" x2="300" y2="270"/><line x1="60" y1="0" x2="60" y2="300"/><line x1="240" y1="0" x2="240" y2="300"/></g></svg>
<div class="step-photo" style="left:226px;top:707px;background:linear-gradient(180deg,#eceeec 0%,#d5d6d2 55%,#7d8a5a 80%,#5f6e43 100%)" role="img" aria-label="Modern two-storey house on a green lawn"></div>
<div class="step-num" style="left:544px;top:790px">01.</div>
<p class="step-text" style="left:612px;top:793px">Tell us what you want to build.<br>Dream home, townhouse, and investment<br>property, whatever.</p>

<!-- step 2 -->
<svg class="guides" style="left:720px;top:922px" viewBox="0 0 300 300"><g stroke="#d5d6d2" stroke-width="1"><line x1="0" y1="40" x2="300" y2="40"/><line x1="0" y1="255" x2="300" y2="255"/><line x1="50" y1="0" x2="50" y2="300"/><line x1="250" y1="0" x2="250" y2="300"/></g></svg>
<div class="step-photo" style="left:755px;top:949px;background:linear-gradient(135deg,#f4f5f7 0%,#b5bfd8 50%,#eef0f4 100%)" role="img" aria-label="Blue architectural floor plan"></div>
<div class="step-num" style="left:610px;top:1032px">02.</div>
<p class="step-text right" style="top:1034px">We'll put a design together for you, or<br>you can choose from a bunch of plans we've<br>already got.</p>

<!-- step 3 -->
<svg class="guides" style="left:186px;top:1140px" viewBox="0 0 300 300"><g stroke="#d5d6d2" stroke-width="1"><line x1="0" y1="40" x2="300" y2="40"/><line x1="0" y1="270" x2="300" y2="270"/><line x1="60" y1="0" x2="60" y2="300"/><line x1="240" y1="0" x2="240" y2="300"/></g></svg>
<div class="step-photo" style="left:226px;top:1165px;background:linear-gradient(160deg,#e3e7ec 0%,#a9b7c6 50%,#5a6468 100%)" role="img" aria-label="Hands working on a calculator beside paperwork"></div>
<div class="step-num" style="left:544px;top:1268px">03.</div>
<p class="step-text" style="left:612px;top:1270px">We'll give you a conservative<br>price estimate.</p>

<!-- step 4 -->
<svg class="guides" style="left:720px;top:1400px" viewBox="0 0 300 300"><g stroke="#d5d6d2" stroke-width="1"><line x1="0" y1="40" x2="300" y2="40"/><line x1="0" y1="255" x2="300" y2="255"/><line x1="50" y1="0" x2="50" y2="300"/><line x1="250" y1="0" x2="250" y2="300"/></g></svg>
<div class="step-photo" style="left:755px;top:1425px;background:linear-gradient(180deg,#a7bcd4 0%,#d2dbe4 45%,#e6e6e2 60%,#b3a68c 100%)" role="img" aria-label="Tradesman's white van parked on a site"></div>
<div class="step-num" style="left:610px;top:1508px">04.</div>
<p class="step-text right" style="top:1510px">We finish tweaking your plans, then send them<br>out to our network of more than 200 builders,<br>subcontractors and tradesmen.</p>

<!-- step 5 -->
<svg class="guides" style="left:186px;top:1640px" viewBox="0 0 300 300"><g stroke="#d5d6d2" stroke-width="1"><line x1="0" y1="40" x2="300" y2="40"/><line x1="0" y1="270" x2="300" y2="270"/><line x1="60" y1="0" x2="60" y2="300"/><line x1="240" y1="0" x2="240" y2="300"/></g></svg>
<div class="step-photo" style="left:226px;top:1666px;background:linear-gradient(135deg,#4e3222 0%,#96582c 45%,#c99544 70%,#6e4127 100%)" role="img" aria-label="Beer being poured from a bar tap"></div>
<div class="step-num" style="left:544px;top:1748px">05.</div>
<p class="step-text" style="left:612px;top:1750px">We collect the quotes, pick the best prices,<br>and finalise your budget. Now you buy us beer,<br>cause you've finally realised how much<br>you're saving.</p>

<!-- step 6 -->
<svg class="guides" style="left:720px;top:1850px" viewBox="0 0 300 300"><g stroke="#d5d6d2" stroke-width="1"><line x1="0" y1="40" x2="300" y2="40"/><line x1="0" y1="255" x2="300" y2="255"/><line x1="50" y1="0" x2="50" y2="300"/><line x1="250" y1="0" x2="250" y2="300"/></g></svg>
<div class="step-photo" style="left:755px;top:1877px;background:linear-gradient(160deg,#e4e5e2 0%,#9a9ea0 55%,#5a6164 100%)" role="img" aria-label="Exterior of the city council building"></div>
<div class="step-num" style="left:610px;top:1988px">06.</div>
<p class="step-text right" style="top:1990px">Tell your friends how awesome we are, while<br>we lodge your building consent application with<br>Council.</p>

<!-- step 7 -->
<svg class="guides" style="left:186px;top:2115px" viewBox="0 0 300 300"><g stroke="#d5d6d2" stroke-width="1"><line x1="0" y1="40" x2="300" y2="40"/><line x1="0" y1="270" x2="300" y2="270"/><line x1="60" y1="0" x2="60" y2="300"/><line x1="240" y1="0" x2="240" y2="300"/></g></svg>
<div class="step-photo" style="left:226px;top:2138px;background:linear-gradient(160deg,#ece4d6 0%,#a7b3c6 45%,#55698a 100%)" role="img" aria-label="Two builders in hard hats reviewing plans on site"></div>
<div class="step-num" style="left:544px;top:2226px">07.</div>
<p class="step-text" style="left:612px;top:2228px">We coordinate the builders and subbies<br>(look, you're already speaking trade-talk) from<br>start to finish. You pay the cost price on their<br>work each month.</p>

<section class="cta-band">
  <h2 class="cta-title">We're happy to talk numbers and give you an estimate.</h2>
  <div class="cta-btn">
    <svg width="14" height="14" viewBox="0 0 24 24"><path d="M6.6 10.8a15.1 15.1 0 0 0 6.6 6.6l2.2-2.2c.3-.3.7-.4 1-.2 1.1.4 2.3.6 3.6.6.6 0 1 .4 1 1V20c0 .6-.4 1-1 1A17 17 0 0 1 3 4c0-.6.4-1 1-1h3.5c.6 0 1 .4 1 1 0 1.3.2 2.5.6 3.6.1.3 0 .7-.2 1z" fill="#ffffff"/></svg>
    Call us
  </div>
</section>

<footer class="site-footer" role="img" aria-label="Dim city skyline at dusk behind the footer">
  <div class="footer-heading" style="left:156px;top:84px">Quick Enquiry</div>
  <div class="field" style="top:140px">Name</div>
  <div class="field" style="top:176px">Phone</div>
  <div class="field" style="top:212px">Email</div>
  <div class="field message" style="top:248px">Type your message</div>
  <div class="send-btn">
    <svg width="12" height="12" viewBox="0 0 12 12"><path d="M0 5 12 0 8 12 6 7z" fill="#fff"/></svg>
    Send your enquiry
  </div>

  <div class="footer-divider"></div>

  <div class="footer-heading" style="left:588px;top:84px">Contact Info</div>
  <div class="contact-row" style="top:128px">
    <svg width="14" height="18" viewBox="0 0 14 18"><path d="M7 0a7 7 0 0 0-7 7c0 5 7 11 7 11s7-6 7-11a7 7 0 0 0-7-7zm0 9.5A2.5 2.5 0 1 1 7 4.5a2.5 2.5 0 0 1 0 5z" fill="#fff"/></svg>
    <div><div class="name">Hollow Fern Builders</div><div class="addr">96 Lorem Ipsum, information<br>random Lipsum (8645)</div></div>
  </div>
  <div class="contact-row" style="top:202px;align-items:center">
    <svg width="16" height="16" viewBox="0 0 24 24"><path d="M6.6 10.8a15.1 15.1 0 0 0 6.6 6.6l2.2-2.2c.3-.3.7-.4 1-.2 1.1.4 2.3.6 3.6.6.6 0 1 .4 1 1V20c0 .6-.4 1-1 1A17 17 0 0 1 3 4c0-.6.4-1 1-1h3.5c.6 0 1 .4 1 1 0 1.3.2 2.5.6 3.6.1.3 0 .7-.2 1z" fill="none" stroke="#fff" stroke-width="1.6"/></svg>
    <span style="font-size:18px">0800 617 280</span>
  </div>
  <div class="contact-row" style="top:240px;align-items:center">
    <svg width="14" height="11" viewBox="0 0 14 11"><rect width="14" height="11" fill="#fff"/><path d="M0 0 7 6 14 0" stroke="#353c3f" fill="none"/></svg>
    <span style="font-size:14px;color:#d5d6d2">info@hollowfernbuilders.com</span>
  </div>

  <svg class="badge" viewBox="0 0 127 221">
    <polygon points="0,0 127,0 127,221 63.5,196 0,221" fill="#ffffff"/>
    <rect x="22" y="34" width="83" height="92" fill="#756897"/>
    <rect x="22" y="138" width="83" height="22" fill="#d5d6d2"/>
  </svg>
</footer>

<div class="bottom-bar">
  <div class="to-top">
    <svg width="38" height="38" viewBox="0 0 38 38"><path d="M13 22 19 16 25 22" stroke="#fff" stroke-width="2" fill="none"/></svg>
  </div>
  <p class="copyright">© Copyright 2016 Hollow Fern Builders.</p>
</div>

</body>
</html>
```